Stationary package for Interior and construction company
Velvet Arch Studios
Professional
Peter Hallsey
Project Manager
Warehouse K42, Dubai Logistics Park Dubai,UAE PO Box 316052
velvetarchdxb@examplemail.test
www.velvetarchdubai.example
We require two business cards with different peoples names. #1 been Peter Hallsey the second persons details are. Simon Ravenholt, Project Manager, Warehouse K42, Dubai Logistics Park, Dubai, UAE, PO Box 316052, Cell- +971 50 6185072 Ph- +971 4 3061825 Email - s.ravenholt@velvetarchstudios.example Web - www.velvetarchstudios.example Brief, Velvet Arch Studios (VAS) is a luxury fit out and renovations company based in Dubai, UAE. VAS’s clientele are high net worth individuals. The company is looking for a suite of stationary to support their everyday business needs; this should include: • Letterheads (page 1 and page2) • Business cards (Two people) • Envelopes (A4, DL) • Notepad (A4, A5) The company would like to evoke a premium brand through chic, clean and sophisticated stationary items. Colour should not be over-used unnecessarily and the typeface should be clear to read. All artwork provided should be re-writable.
Please just use the logo, add the website to the bottom footer. open to options on layout and design.

```html
<!DOCTYPE html>
<html lang="en">
<head>
<meta charset="utf-8">
<title>Velvet Arch Studios – Business Cards</title>
<link rel="stylesheet" href="https://fonts.googleapis.com/css2?family=Montserrat:wght@400;600;700&family=Open+Sans:wght@400;600&display=swap">
<style>
  :root {
    --bg: #d9d9d9;
    --card: #ffffff;
    --brand-blue: #2a90d2;
    --brand-grey: #6d6e71;
    --frame: #8a8a8a;
    --text: #4a4a4a;
    --white: #ffffff;
  }
  * { box-sizing: border-box; margin: 0; padding: 0; }
  html, body { width: 1200px; height: 895px; overflow: hidden; }
  body {
    background: var(--bg);
    position: relative;
    font-family: "Open Sans", Arial, sans-serif;
    color: var(--text);
  }
  .card {
    position: absolute;
    width: 620px;
    height: 354px;
    background: var(--card);
    box-shadow: 0 4px 14px rgba(0,0,0,0.18);
    overflow: hidden;
  }
  .card-frame {
    position: absolute;
    inset: 16px;
    border: 2px solid var(--frame);
    z-index: 3;
    pointer-events: none;
  }

  /* Back of card */
  .card-back { left: 530px; top: 60px; }
  .card-back .brand-mark {
    position: absolute;
    left: 0; right: 0; top: 92px;
    display: flex;
    justify-content: center;
    align-items: center;
    gap: 14px;
    font-family: "Montserrat", Arial, sans-serif;
    font-weight: 700;
    font-size: 64px;
    letter-spacing: 4px;
    color: var(--brand-grey);
  }
  .brand-dot {
    width: 22px; height: 22px;
    border-radius: 50%;
    background: var(--brand-blue);
  }
  .card-back .footer-band {
    position: absolute;
    left: 0; right: 0; top: 232px;
    height: 54px;
    background: var(--brand-blue);
    color: var(--white);
    font-family: "Montserrat", Arial, sans-serif;
    font-size: 21px;
    letter-spacing: 1px;
    display: flex;
    align-items: center;
    justify-content: center;
  }

  /* Front of card */
  .card-front { left: 50px; top: 440px; }
  .card-front .brand-name {
    position: absolute;
    left: 40px; top: 40px;
    display: flex; align-items: center; gap: 10px;
    font-family: "Montserrat", Arial, sans-serif;
    font-weight: 600;
    font-size: 24px;
    color: var(--brand-blue);
  }
  .card-front .brand-name .brand-dot { width: 16px; height: 16px; }
  .side-band {
    position: absolute;
    left: 0; top: 110px;
    width: 250px; height: 26px;
    background: var(--brand-blue);
  }
  .footer-band-front {
    position: absolute;
    left: 0; right: 0; bottom: 0;
    height: 30px;
    background: var(--brand-blue);
  }
  .person {
    position: absolute;
    right: 48px; top: 116px;
    text-align: right;
  }
  .person-name {
    font-family: "Montserrat", Arial, sans-serif;
    font-size: 22px;
    font-weight: 600;
    color: var(--brand-blue);
  }
  .person-role { font-size: 14px; color: var(--text); margin-top: 2px; }
  .contact-list {
    position: absolute;
    list-style: none;
    font-size: 13px;
    line-height: 1.3;
  }
  .contact-list li { display: flex; align-items: flex-start; gap: 10px; margin-bottom: 12px; }
  .contact-left { left: 40px; top: 160px; }
  .contact-right { left: 330px; top: 196px; width: 250px; }
  .icon {
    flex: 0 0 20px;
    width: 20px; height: 20px;
    background: var(--brand-blue);
    border-radius: 3px;
    display: flex; align-items: center; justify-content: center;
  }
  .icon svg { width: 13px; height: 13px; }
</style>
</head>
<body>

  <section class="card card-back" aria-label="Business card back">
    <div class="brand-mark"><span class="brand-dot"></span>VAS</div>
    <div class="footer-band">www.velvetarchdubai.example</div>
    <div class="card-frame"></div>
  </section>

  <section class="card card-front" aria-label="Business card front">
    <div class="brand-name"><span class="brand-dot"></span>Velvet Arch Studios</div>
    <div class="side-band"></div>

    <div class="person">
      <p class="person-name">Peter Hallsey</p>
      <p class="person-role">Project Manager</p>
    </div>

    <ul class="contact-list contact-left">
      <li>
        <span class="icon"><svg viewBox="0 0 16 16"><path fill="#fff" d="M3.5 1.5l2.5 0 1 3.5-1.8 1.2a8 8 0 0 0 4.6 4.6L11 9l3.5 1v2.5c0 1-1 2-2 2C7 14.5 1.5 9 1.5 3.5c0-1 1-2 2-2z"/></svg></span>
        <span>+971 4 3061825</span>
      </li>
      <li>
        <span class="icon"><svg viewBox="0 0 16 16"><rect x="1.5" y="3.5" width="13" height="9" fill="none" stroke="#fff" stroke-width="1.5"/><path d="M1.5 3.5l6.5 5 6.5-5" fill="none" stroke="#fff" stroke-width="1.5"/></svg></span>
        <span>velvetarchdxb@examplemail.test</span>
      </li>
    </ul>

    <ul class="contact-list contact-right">
      <li>
        <span class="icon"><svg viewBox="0 0 16 16"><path fill="#fff" d="M8 1a5 5 0 0 0-5 5c0 3.8 5 9 5 9s5-5.2 5-9a5 5 0 0 0-5-5zm0 7a2 2 0 1 1 0-4 2 2 0 0 1 0 4z"/></svg></span>
        <span>Warehouse K42, Dubai Logistics Park<br>Dubai, UAE, PO Box 316052</span>
      </li>
      <li>
        <span class="icon"><svg viewBox="0 0 16 16"><circle cx="8" cy="8" r="6.2" fill="none" stroke="#fff" stroke-width="1.4"/><path d="M1.8 8h12.4M8 1.8c-3 3.5-3 8.9 0 12.4M8 1.8c3 3.5 3 8.9 0 12.4" fill="none" stroke="#fff" stroke-width="1.2"/></svg></span>
        <span>www.velvetarchdubai.example</span>
      </li>
    </ul>

    <div class="footer-band-front"></div>
    <div class="card-frame"></div>
  </section>

</body>
</html>
```